Business card for my new company (Accounting firm)

I need a business card for my new business Corvane Advisory and Ledger SA. Our services are accounting, tax, audit and financial management. Our customers are small companies, start-ups and new companies. The final design has to show financial security, trust and growth. Please find our logo attached to the business card. Text for the business card: Corvane Advisory and Ledger SA Tomas da Varela Director and Founder Certified Accountant Tel. 022 418 27 35 tv@corvaneconseil.ch www.corvaneconseil.ch Rue des Vergers-Bleus 14 1201 Geneva
Target Market(s)
Our customers are small companies, start-ups and new companies.
Industry/Entity Type
Finance And Accounting
Contact Information for Business Card
Corvane Conseil et Registre SA
Tomas da Varela
Directeur et Fondateur
Expert-comptable diplômé
Tél. 022 418 27 35
tv@corvaneconseil.ch
www.corvaneconseil.ch
Rue des Vergers-Bleus 14
1201 Genève

```html
<!DOCTYPE html>
<html lang="fr">
<head>
<meta charset="utf-8">
<title>Corvane Conseil et Registre SA – Carte de visite</title>
<link rel="stylesheet" href="https://fonts.googleapis.com/css2?family=Montserrat:wght@600&family=Roboto:wght@400;500&family=Roboto+Condensed:wght@400&family=Teko:wght@400&display=swap">
<style>
  :root {
    --page: #ffffff;
    --ice: #eef8fa;
    --brand-blue: #2f80f2;
    --deep-blue: #1b63c9;
    --ink: #2a3336;
    --white: #ffffff;
  }
  * { margin: 0; padding: 0; box-sizing: border-box; }
  html, body {
    width: 1200px; height: 621px; overflow: hidden;
    background: var(--page);
  }
  .canvas { position: relative; width: 1200px; height: 621px; }

  .card-front {
    position: absolute; left: 106px; top: 185px; width: 465px; height: 291px;
    background: var(--ice);
  }
  .card-back {
    position: absolute; left: 571px; top: 185px; width: 464px; height: 291px;
    background: var(--brand-blue);
  }
  .line { position: absolute; line-height: 1; white-space: nowrap; }

  /* front */
  .brand-mark {
    position: absolute; left: 24px; top: 130px;
    display: flex; align-items: center; gap: 12px;
  }
  .brand-square { width: 26px; height: 26px; background: var(--brand-blue); }
  .brand-name {
    font-family: "Montserrat", sans-serif; font-weight: 600;
    font-size: 38px; letter-spacing: 2px; color: var(--ink); line-height: 1;
  }
  .front-company {
    right: 20px; top: 196px;
    font-family: "Roboto", sans-serif; font-weight: 500;
    font-size: 14.5px; letter-spacing: 1px; color: var(--brand-blue);
  }
  .name-band { position: absolute; left: 0; top: 0; }
  .front-name {
    right: 16px; top: 219px;
    font-family: "Teko", sans-serif; font-weight: 400;
    font-size: 30px; letter-spacing: 4px; color: var(--white);
  }
  .front-role {
    right: 14px; top: 257px;
    font-family: "Roboto", sans-serif; font-size: 12px;
    letter-spacing: 4.6px; color: var(--deep-blue);
  }

  /* back */
  .address {
    left: 10px; top: 22px;
    font-family: "Roboto", sans-serif; font-size: 12px;
    letter-spacing: 2px; color: var(--white); line-height: 23px;
  }
  .contact-block { position: absolute; right: 10px; top: 20px; text-align: right; color: var(--white); }
  .back-name {
    font-family: "Teko", sans-serif; font-size: 28px; letter-spacing: 3.5px; line-height: 1;
  }
  .back-role {
    font-family: "Roboto", sans-serif; font-size: 12px; letter-spacing: 2px; margin-top: 0px;
  }
  .back-credential {
    font-family: "Roboto Condensed", sans-serif; font-size: 13px; letter-spacing: 1px; margin-top: 6px;
  }
  .back-phone {
    font-family: "Roboto", sans-serif; font-size: 15px; letter-spacing: 2px; margin-top: 5px;
  }
  .company-band {
    position: absolute; left: 0; top: 211px; width: 100%; height: 39px;
    background: var(--ice);
    display: flex; align-items: center; justify-content: center;
    font-family: "Roboto", sans-serif; font-weight: 500;
    font-size: 17px; letter-spacing: 2px; color: var(--brand-blue);
  }
  .web-row {
    position: absolute; left: 0; top: 256px; width: 100%;
    display: flex; justify-content: center; align-items: center; gap: 14px;
    font-family: "Roboto", sans-serif; font-size: 13.5px; letter-spacing: 1.5px; color: var(--white);
  }
  .web-divider { width: 1.5px; height: 18px; background: var(--white); }
</style>
</head>
<body>
<div class="canvas">
  <section class="card-front">
    <div class="brand-mark">
      <span class="brand-square"></span>
      <span class="brand-name">CORVANE</span>
    </div>
    <div class="line front-company">CORVANE CONSEIL ET REGISTRE SA</div>
    <svg class="name-band" width="465" height="291" aria-hidden="true">
      <polygon points="217,211 465,211 465,250 240,250" fill="var(--brand-blue)"/>
    </svg>
    <div class="line front-name">TOMAS DA VARELA</div>
    <div class="line front-role">Directeur et Fondateur</div>
  </section>

  <section class="card-back">
    <div class="line address">Rue des Vergers-Bleus 14<br>1201 Genève</div>
    <div class="contact-block">
      <div class="back-name">TOMAS DA VARELA</div>
      <div class="back-role">Directeur et Fondateur</div>
      <div class="back-credential">Expert-comptable diplômé</div>
      <div class="back-phone">Tel. 022 418 27 35</div>
    </div>
    <div class="company-band">CORVANE CONSEIL ET REGISTRE SA</div>
    <div class="web-row">
      <span>tv@corvaneconseil.ch</span>
      <span class="web-divider"></span>
      <span>www.corvaneconseil.ch</span>
    </div>
  </section>
</div>
</body>
</html>
```